XVQ Structural Approval Standards Private Assessors

Professional Construction Consultancy Company Business Card - must keep logo colours see images below - examples have been added from my last competition - please see them as examples only!

Target Market(s)

Home Builders

Industry/Entity Type

Construction

Contact Information for Business Card

See "must haves"

Font styles to use
Sans Serif

Colors
ffffff
add136
000000

Requirements
Must have
• Daniel Moravi
• Director
• Phone: 0431 587 219
• Address: 7 Tarrunga Rd,
• Hallworth Vale, SA, 5091
• Email: xvqassessors@mailbox-example.com
• Website: www.xvqassessors-example.com.au
• Facebook: XVQ Structural Approval Standards
Nice to have
• Side 1: full logo
• Side 2: company details
Should not have
• hard to read
• must be clear and professional

```html
<!DOCTYPE html>
<html lang="en">
<head>
<meta charset="utf-8">
<title>XVQ Structural Approval Standards — Business Card</title>
<link href="https://fonts.googleapis.com/css2?family=Montserrat:wght@700&family=Questrial&display=swap" rel="stylesheet">
<style>
  :root {
    --brand-green: #add136;
    --ink: #000000;
    --paper: #ffffff;
    --backdrop: #3a3a3a;
    --muted: #555555;
  }
  * { margin: 0; padding: 0; box-sizing: border-box; }
  html, body { width: 1200px; height: 900px; overflow: hidden; }
  body {
    background: var(--backdrop);
    font-family: "Questrial", "Century Gothic", sans-serif;
    position: relative;
  }
  .card {
    position: absolute;
    left: 290px;
    width: 620px;
    height: 354px;
    overflow: hidden;
    box-shadow: 0 10px 30px rgba(0,0,0,.45);
  }
  /* ---------- Side 1: logo side ---------- */
  .card--logo { top: 70px; background: var(--ink); }
  .card--logo .brand { position: absolute; left: 0; right: 0; top: 100px; display: flex; justify-content: center; align-items: center; gap: 16px; }
  .card--logo .website { position: absolute; left: 0; right: 0; top: 262px; text-align: center; color: var(--paper); font-size: 15px; letter-spacing: .3px; }

  .brand__mark { width: 56px; height: 56px; background: var(--brand-green); flex: none; }
  .brand__name {
    font-family: "Montserrat", sans-serif;
    font-weight: 700;
    color: var(--brand-green);
    text-transform: uppercase;
    line-height: 1.1;
  }
  .brand__name .lead { display: block; font-size: 40px; letter-spacing: 2px; }
  .brand__name .line { display: block; font-size: 13px; letter-spacing: 1px; }
  .brand__name .sub { display: block; font-size: 11px; letter-spacing: 6px; margin-top: 4px; }

  /* ---------- Side 2: details side ---------- */
  .card--details { top: 476px; background: var(--paper); }
  .card--details .brand { position: absolute; right: 28px; top: 26px; display: flex; align-items: center; gap: 12px; }
  .card--details .brand__mark { width: 40px; height: 40px; }
  .card--details .brand__name { color: var(--ink); }
  .card--details .brand__name .lead { font-size: 30px; }
  .card--details .brand__name .line { font-size: 10px; }
  .card--details .brand__name .sub { font-size: 9px; letter-spacing: 4.5px; }

  .person { position: absolute; left: 36px; top: 112px; }
  .person__name { font-family: "Montserrat", sans-serif; font-weight: 700; font-size: 19px; letter-spacing: .5px; color: var(--ink); text-transform: uppercase; }
  .person__role { font-size: 15px; color: var(--muted); margin-top: 2px; }

  .panel { position: absolute; left: 0; right: 0; top: 178px; bottom: 0; background: var(--ink); }
  .panel__notch { position: absolute; left: 120px; top: -10px; width: 0; height: 0; border-left: 10px solid transparent; border-right: 10px solid transparent; border-bottom: 10px solid var(--ink); }
  .panel__stripe { position: absolute; left: 0; right: 0; bottom: 18px; height: 26px; background: var(--brand-green); }

  .address { position: absolute; right: 28px; top: 16px; text-align: right; color: var(--paper); font-size: 13px; line-height: 1.45; }

  .contacts { position: absolute; left: 36px; top: 40px; list-style: none; color: var(--paper); font-size: 13px; }
  .contacts li { display: flex; align-items: center; gap: 10px; height: 22px; }
  .contacts .icon { width: 16px; height: 16px; background: var(--brand-green); border-radius: 3px; flex: none; display: flex; align-items: center; justify-content: center; }
  .contacts svg { width: 11px; height: 11px; }
</style>
</head>
<body>

<section class="card card--logo" aria-label="Card side 1">
  <div class="brand">
    <span class="brand__mark" aria-hidden="true"></span>
    <p class="brand__name">
      <span class="lead">XVQ</span>
      <span class="line">Structural Approval Standards</span>
      <span class="sub">Private Assessors</span>
    </p>
  </div>
  <p class="website">www.xvqassessors-example.com.au</p>
</section>

<section class="card card--details" aria-label="Card side 2">
  <div class="brand">
    <span class="brand__mark" aria-hidden="true"></span>
    <p class="brand__name">
      <span class="lead">XVQ</span>
      <span class="line">Structural Approval Standards</span>
      <span class="sub">Private Assessors</span>
    </p>
  </div>

  <div class="person">
    <p class="person__name">Daniel Moravi</p>
    <p class="person__role">Director</p>
  </div>

  <div class="panel">
    <span class="panel__notch" aria-hidden="true"></span>
    <p class="address">7 Tarrunga Rd,<br>Hallworth Vale,<br>SA, 5091</p>
    <ul class="contacts">
      <li><span class="icon"><svg viewBox="0 0 12 12"><rect x="3" y="1" width="6" height="10" rx="1" fill="none" stroke="#000" stroke-width="1.3"/></svg></span>0431 587 219</li>
      <li><span class="icon"><svg viewBox="0 0 12 12"><rect x="1" y="2.5" width="10" height="7" fill="none" stroke="#000" stroke-width="1.2"/><path d="M1 2.5 L6 6.5 L11 2.5" fill="none" stroke="#000" stroke-width="1.2"/></svg></span>xvqassessors@mailbox-example.com</li>
      <li><span class="icon"><svg viewBox="0 0 12 12"><circle cx="6" cy="6" r="4.6" fill="none" stroke="#000" stroke-width="1.1"/><ellipse cx="6" cy="6" rx="2" ry="4.6" fill="none" stroke="#000" stroke-width="1"/><path d="M1.4 6 H10.6" stroke="#000" stroke-width="1"/></svg></span>www.xvqassessors-example.com.au</li>
      <li><span class="icon" aria-hidden="true"></span>XVQ Structural Approval Standards</li>
    </ul>
    <span class="panel__stripe" aria-hidden="true"></span>
  </div>
</section>

</body>
</html>
```